Design a Word Template and Powerpoint Template for a Venture Capital Fund

I'm looking to get a powerpoint template and word template designed ASAP under the same selected design. Its for a finance / Venture Capital business... keen to keep it clean but "pop" and stand up on its own as a strong brand, solid templates etc... Happy to talk. Thanks Kit

Target Market(s)

Venture Capital and Private Equity

Industry/Entity Type

Finance / Venture Capital / Management Consulting

Requirements
Nice to have
• Strong formatting, icons and optionality, images can be good too

```html
<!DOCTYPE html>
<html lang="en">
<head>
<meta charset="utf-8">
<title>Seedline Capital Partners – Stationery and Slides</title>
<link href="https://fonts.googleapis.com/css2?family=Josefin+Sans:wght@300&family=Roboto+Condensed:wght@400;700&family=Arimo:wght@400&display=swap" rel="stylesheet">
<style>
:root{
  --board:#a3a3a3;
  --paper:#fafafa;
  --ink:#2a2a2a;
  --ink-soft:#555;
  --muted:#8a8a8a;
  --rule:#9a9a9a;
  --dark-slide:#2b2a2b;
  --photo:#4a4a4a;
  --pie-light:#8c8c8c;
}
*{margin:0;padding:0;box-sizing:border-box}
html,body{width:1200px;height:766px;overflow:hidden;background:var(--board)}
body{position:relative;font-family:"Arimo",Arial,sans-serif;color:var(--ink)}
.sheet{position:absolute;background:var(--paper);box-shadow:2px 3px 5px rgba(0,0,0,.35)}

/* Letterhead */
.letter{left:73px;top:62px;width:454px;height:637px;background:linear-gradient(135deg,#fbfbfb 0%,#f3f3f3 60%,#ececec 100%)}
.brand{position:absolute;font-family:"Josefin Sans",sans-serif;font-weight:300;color:var(--ink);letter-spacing:1px;white-space:nowrap}
.letter .brand{left:34px;top:56px;font-size:13px}
.letter .brand-rule{position:absolute;left:34px;top:74px;width:150px;border-top:1px solid var(--ink-soft)}
.contact{position:absolute;left:352px;top:47px;font-size:6px;line-height:9.6px;color:var(--ink-soft)}
.contact li{list-style:none;display:flex;align-items:center;gap:4px}
.contact .icon{width:5px;height:5px;background:var(--ink);border-radius:1px;display:inline-block}
.salutation{position:absolute;left:34px;top:160px;font-size:11px;color:var(--ink-soft)}
.letter-body{position:absolute;left:34px;top:193px;width:386px;font-size:6.2px;line-height:9.4px;color:var(--ink-soft);text-align:justify}
.letter-body p{margin-bottom:10px}
.signoff{position:absolute;left:34px;top:406px;font-size:6.2px;color:var(--ink-soft)}
.signature{position:absolute;left:31px;top:430px;width:130px;height:30px;background:linear-gradient(90deg,rgba(40,40,40,.18),rgba(40,40,40,.05))}

/* Slides */
.slide{width:266px;height:200px;overflow:hidden}
.col1{left:579px}.col2{left:865px}
.row1{top:61px}.row2{top:278px}.row3{top:498px}
.slide-head{position:absolute;left:14px;top:11px;font-family:"Roboto Condensed",sans-serif}
.slide-head h2{font-size:11.5px;font-weight:700;color:var(--ink);line-height:1.1}
.slide-head p{font-size:6px;color:var(--muted);font-weight:700}
.head-rule{position:absolute;left:58px;right:14px;top:31px;border-top:1px solid var(--rule)}
.slide .mini-brand{position:absolute;right:14px;top:14px;font-family:"Josefin Sans",sans-serif;font-weight:300;font-size:7px;color:var(--ink)}
.tiny{font-size:3.6px;line-height:5.2px;color:var(--ink-soft);text-align:justify}

/* Title slide */
.title-slide .brand{left:0;right:0;top:54px;text-align:center;font-size:11px}
.title-slide .brand-rule{position:absolute;left:83px;top:70px;width:100px;border-top:1px solid var(--ink-soft)}
.welcome{position:absolute;left:0;right:0;top:118px;text-align:center;font-family:"Roboto Condensed",sans-serif;color:var(--muted)}
.welcome .lead{font-size:13px;line-height:17px}
.welcome .name{font-size:15px;font-weight:700;color:var(--ink);line-height:17px}
.welcome .desc{font-size:12px;line-height:17px}

/* Team slide */
.team{position:absolute;left:19px;top:56px;display:flex;gap:6px}
.member{width:52px}
.photo{width:52px;height:52px;background:var(--photo);border:2px solid #fff;box-shadow:0 0 2px rgba(0,0,0,.4);color:#ccc;font-size:6px;display:flex;align-items:center;justify-content:center}
.member h3{margin-top:11px;font-size:5px;font-weight:700;font-family:"Roboto Condensed",sans-serif}
.member .role{font-size:4px;color:var(--muted);font-style:italic;margin:2px 0 8px}

/* Groups slide */
.groups{position:absolute;left:15px;top:49px;display:grid;grid-template-columns:114px 114px;column-gap:7px;row-gap:9px}
.groups h3{font-family:"Roboto Condensed",sans-serif;font-size:6px;font-weight:700;margin-bottom:3px}

/* Chart slide */
.bar-chart{position:absolute;left:24px;top:48px}
.chart-notes{position:absolute;left:161px;top:50px;width:80px;font-size:3.8px;line-height:5.2px;color:var(--ink-soft)}
.chart-notes p{margin-bottom:4px}
.chart-summary{position:absolute;left:21px;top:148px;width:226px}

/* Pie slide */
.pie-text{position:absolute;left:18px;top:64px;width:114px;text-align:right}
.pie-text p{margin-bottom:10px;text-align:right}
.pie{position:absolute;left:164px;top:56px}
.legend{position:absolute;left:163px;top:127px;width:72px;font-size:3.6px;color:var(--ink-soft)}
.legend li{list-style:none;display:flex;align-items:center;gap:3px;border-bottom:.6px solid var(--ink-soft);padding:1.5px 0}
.legend .swatch{width:4px;height:4px;display:inline-block}
.legend-note{position:absolute;left:163px;top:150px;width:72px;text-align:left}

/* Closing slide */
.closing{background:var(--dark-slide);color:#fff;text-align:center}
.closing .thanks{position:absolute;left:0;right:0;top:66px;font-family:"Josefin Sans",sans-serif;font-weight:300;font-size:39px;line-height:42px}
.closing .coming{position:absolute;left:0;right:0;top:108px;font-family:"Josefin Sans",sans-serif;font-weight:300;font-size:21px}
.closing .details{position:absolute;left:0;right:0;top:172px;font-size:5px}
</style>
</head>
<body>

<section class="sheet letter" aria-label="Letterhead">
  <div class="brand">Seedline Capital Partners</div>
  <div class="brand-rule"></div>
  <ul class="contact">
    <li><span class="icon"></span>+61 400-555-123</li>
    <li><span class="icon"></span>kit@northwellmail.com</li>
    <li><span class="icon"></span>www.seedlinecap.com.au</li>
  </ul>
  <p class="salutation">Dear Mr. Harlow,</p>
  <div class="letter-body">
    <p>Lorem ipsum dolor sit amet, consectetur adipiscing elit. Donec orci purus, luctus vitae dignissim eu, iaculis sed purus. Vivamus faucibus, ipsum nec aliquet viverra, leo mauris condimentum ligula, sit amet sagittis enim ligula quis arcu. Nam egestas tortor id nisi porttitor mattis. In tortor ante, ultricies in suscipit a, tempus non massa. Vivamus et auctor mi. Fusce vel massa nulla. Phasellus nec eros mauris, et scelerisque orci.</p>
    <p>Donec malesuada orci vitae nulla accumsan porta a id massa. Quisque accumsan iaculis magna sit amet fringilla. Maecenas consequat, magna eget tincidunt semper, odio nibh rutrum mi, id feugiat ante nisi eu risus. Vestibulum nunc orci, rhoncus a placerat in, ultricies in mi. Cras mattis varius eros, vel fringilla nisi suscipit eget. Quisque scelerisque sagittis nulla at porttitor.</p>
    <p>Sed id augue vitae urna euismod commodo aliquet a quam. Pellentesque arcu velit, cursus et malesuada ut, consequat et diam. Nullam erat sem, rhoncus id ullamcorper vitae, rhoncus et arcu. In ultricies ultricies nulla, ut rutrum nisi iaculis at. Donec eu magna a metus ornare faucibus. Fusce aliquet faucibus ultricies. Morbi semper, est id tincidunt gravida, sem arcu adipiscing lacus, ac bibendum nulla leo eu purus. Quisque nec diam sed risus consectetur accumsan quis quis nibh. Vestibulum id purus lorem.</p>
    <p>It is a long established fact that a reader will be distracted by the readable content of a page when looking at its layout. The point of using Lorem Ipsum is that it has a more-or-less normal distribution of letters, as opposed to using 'Content here, content here', making it look like readable English. Many desktop publishing packages</p>
    <p>ada ut, consequat et diam. Nullam erat sem, rhoncus id ullamcorper vitae, rhoncus et arcu. In ultricies ultricies nulla, ut rutrum nisi iaculis at. Donec eu magna a metus ornare faucibus. Fusce aliquet faucibus ultricies. Morbi semper,</p>
  </div>
  <p class="signoff">Sincerely,</p>
  <div class="signature" role="img" aria-label="Handwritten signature"></div>
</section>

<section class="sheet slide title-slide col1 row1" aria-label="Title slide">
  <div class="brand">Seedline Capital Partners</div>
  <div class="brand-rule"></div>
  <div class="welcome">
    <p class="lead">Welcome to Our</p>
    <p class="name">Presentation Name</p>
    <p class="desc">Description</p>
  </div>
</section>

<section class="sheet slide col2 row1" aria-label="Team slide">
  <div class="slide-head"><h2>Heading Here</h2><p>Sub Heading</p></div>
  <div class="head-rule"></div>
  <div class="mini-brand">Seedline</div>
  <div class="team">
    <div class="member"><div class="photo" role="img" aria-label="Team member photo">Photo</div><h3>Team member1</h3><p class="role">Title</p><p class="tiny">Brief note on role, focus and past deals.</p></div>
    <div class="member"><div class="photo" role="img" aria-label="Team member photo">Photo</div><h3>Team member2</h3><p class="role">Title</p><p class="tiny">Leads research and sector review for new funds.</p></div>
    <div class="member"><div class="photo" role="img" aria-label="Team member photo">Photo</div><h3>Team member3</h3><p class="role">Title</p><p class="tiny">Manages investor relations and quarterly fund reports.</p></div>
    <div class="member"><div class="photo" role="img" aria-label="Team member photo">Photo</div><h3>Team member4</h3><p class="role">Title</p><p class="tiny">Oversees legal terms, compliance and deal closing.</p></div>
  </div>
</section>

<section class="sheet slide col1 row2" aria-label="Groups slide">
  <div class="slide-head"><h2>Heading Here</h2><p>Sub Heading</p></div>
  <div class="head-rule"></div>
  <div class="mini-brand">Seedline</div>
  <div class="groups">
    <div><h3>Group1</h3><p class="tiny">Short summary of this group, its aims, key figures and the next steps agreed by the team.</p></div>
    <div><h3>Group4</h3><p class="tiny">Short summary of this group, its aims, key figures and the next steps agreed by the team.</p></div>
    <div><h3>Group2</h3><p class="tiny">Short summary of this group, its aims, key figures and the next steps agreed by the team.</p></div>
    <div><h3>Group5</h3><p class="tiny">Short summary of this group, its aims, key figures and the next steps agreed by the team.</p></div>
    <div><h3>Group3</h3><p class="tiny">Short summary of this group, its aims, key figures and the next steps agreed by the team.</p></div>
    <div><h3>Group6</h3><p class="tiny">Short summary of this group, its aims, key figures and the next steps agreed by the team.</p></div>
  </div>
</section>

<section class="sheet slide col2 row2" aria-label="Bar chart slide">
  <div class="slide-head"><h2>Heading Here</h2><p>Sub Heading</p></div>
  <div class="head-rule"></div>
  <div class="mini-brand">Seedline</div>
  <svg class="bar-chart" width="110" height="86" viewBox="0 0 110 86" aria-label="Bar chart">
    <g stroke="#c8c8c8" stroke-width=".5">
      <line x1="0" y1="6" x2="106" y2="6"/><line x1="0" y1="12" x2="106" y2="12"/>
      <line x1="0" y1="18" x2="106" y2="18"/><line x1="0" y1="24" x2="106" y2="24"/>
      <line x1="0" y1="30" x2="106" y2="30"/><line x1="0" y1="36" x2="106" y2="36"/>
      <line x1="0" y1="42" x2="106" y2="42"/><line x1="0" y1="48" x2="106" y2="48"/>
      <line x1="0" y1="54" x2="106" y2="54"/><line x1="0" y1="60" x2="106" y2="60"/>
      <line x1="0" y1="66" x2="106" y2="66"/><line x1="0" y1="72" x2="106" y2="72"/>
      <line x1="0" y1="78" x2="106" y2="78"/>
    </g>
    <g fill="#2a2a2a">
      <rect x="26" y="4" width="13" height="78"/>
      <rect x="42" y="15" width="13" height="67"/>
      <rect x="58" y="34" width="13" height="48"/>
      <rect x="73" y="21" width="13" height="61"/>
    </g>
    <g fill="#fff" font-size="3.6" font-family="Arimo, sans-serif">
      <text transform="translate(34 80) rotate(-90)">Sub text1</text>
      <text transform="translate(50 80) rotate(-90)">Sub text2</text>
      <text transform="translate(66 80) rotate(-90)">Sub text3</text>
      <text transform="translate(81 80) rotate(-90)">Sub text4</text>
    </g>
  </svg>
  <div class="chart-notes">
    <p>Key point on fund growth across the period shown here.</p>
    <p>Returns rose in early rounds and held steady after.</p>
  </div>
  <p class="tiny chart-summary">Summary of results for the year, with notes on each stage and what drove the change in value across the portfolio.</p>
</section>

<section class="sheet slide col1 row3" aria-label="Pie chart slide">
  <div class="slide-head"><h2>Heading Here</h2><p>Sub Heading</p></div>
  <div class="head-rule"></div>
  <div class="mini-brand">Seedline</div>
  <div class="pie-text tiny">
    <p>Overview of how capital is split across sectors, with notes on the largest holdings, the smaller positions and the plan for new commitments over the coming year.</p>
    <p>Further detail on timing and risk for each sector.</p>
  </div>
  <svg class="pie" width="62" height="62" viewBox="-31 -31 62 62" aria-label="Pie chart">
    <g stroke="#fafafa" stroke-width=".8">
      <path d="M0 0 L5 28.6 A29 29 0 0 1 -5 -28.6 Z" fill="#2a2a2a"/>
      <path d="M0 0 L-5 -28.6 A29 29 0 0 1 28.6 -5 Z" fill="var(--pie-light)"/>
      <path d="M0 0 L28.6 -5 A29 29 0 0 1 25.1 14.5 Z" fill="#2a2a2a"/>
      <path d="M0 0 L25.1 14.5 A29 29 0 0 1 5 28.6 Z" fill="var(--pie-light)"/>
    </g>
  </svg>
  <ul class="legend">
    <li><span class="swatch" style="background:#2a2a2a"></span>Sector A share 50%</li>
    <li><span class="swatch" style="background:var(--pie-light)"></span>Sector B share 50%</li>
  </ul>
  <p class="tiny legend-note">Figures as at the last quarter end.</p>
</section>

<section class="sheet slide closing col2 row3" aria-label="Closing slide">
  <p class="thanks">Thanks</p>
  <p class="coming">For Coming</p>
  <p class="details">P: +61 400-555-123 E: kit@northwellmail.com W: seedlinecap.com.au</p>
</section>

</body>
</html>
```